Buch-/eBook-Cover für Sachbuch gesucht
Zielgruppe
We're selfpublishing nonfiction books. Interested are adults - mostly man (age range: 25-50) - who want to learn more about leadership at their workplaces.
Aufgabenstellung
The design should be clean and simple, title easy to read, good color contrast (the cover has to stand out from an white background).

```html
<!DOCTYPE html>
<html lang="en">
<head>
<meta charset="utf-8">
<title>Leadership – Book Cover</title>
<link href="https://fonts.googleapis.com/css2?family=Kaushan+Script&family=Oswald:wght@500;600&display=swap" rel="stylesheet">
<style>
  :root {
    --backdrop: #ececec;
    --gold-light: #f1d469;
    --gold-mid: #e2b52b;
    --gold-deep: #c8961a;
    --gold-dark: #b5861a;
    --ink: #141210;
  }
  * { margin: 0; padding: 0; box-sizing: border-box; }
  html, body {
    width: 1200px;
    height: 1200px;
    overflow: hidden;
    background: var(--backdrop);
  }
  .canvas {
    position: relative;
    width: 1200px;
    height: 1200px;
  }
  .cover {
    position: absolute;
    left: 215px;
    top: 50px;
    width: 770px;
    height: 1100px;
    background:
      radial-gradient(ellipse at 75% 20%, rgba(255, 240, 170, 0.55) 0%, rgba(255, 240, 170, 0) 55%),
      linear-gradient(175deg, var(--gold-light) 0%, var(--gold-mid) 45%, var(--gold-deep) 80%, var(--gold-dark) 100%);
    color: var(--ink);
    text-align: center;
  }
  .cover__title {
    position: absolute;
    top: 195px;
    left: 0;
    right: 0;
    font-family: "Kaushan Script", cursive;
    font-weight: 400;
    font-size: 150px;
    line-height: 1;
    letter-spacing: -1px;
  }
  .cover__subtitle {
    position: absolute;
    top: 405px;
    left: 0;
    right: 0;
    font-family: "Oswald", sans-serif;
    font-weight: 600;
    font-size: 44px;
    line-height: 56px;
    text-transform: uppercase;
    letter-spacing: 0.3px;
  }
  .cover__author {
    position: absolute;
    top: 1015px;
    left: 0;
    right: 0;
    font-family: "Oswald", sans-serif;
    font-weight: 500;
    font-size: 27px;
    line-height: 1;
    text-transform: uppercase;
    letter-spacing: 0.3px;
  }
</style>
</head>
<body>
  <main class="canvas">
    <section class="cover">
      <h1 class="cover__title">Leadership</h1>
      <p class="cover__subtitle">Fostering Growth<br>and Inspiring Excellence</p>
      <p class="cover__author">Daniel Harwick</p>
    </section>
  </main>
</body>
</html>
```